Modern, eye catching eliquid bottle label. 1.5 x 2.75

We need a label design for our e-juice bottles. The labels to be printed are 1.5 inches in height and 2.75 inches in width. We are looking to include our website (www.quillbrookmistparlor.com) and our phone number of 2 different shops. The most prominent thing needs to be our logo(attached .pdf and jpeg). We will need 2 spots that we can edit on an ongoing basis for nicotine strength and the flavor. We want something simplistic but eye-catching. Our colors are Purple, Red, and Orange. We would also like our website fairly prominent as well.

Target Market(s)

18-45 vapers and e-cigarette users

Font styles to use
Serif

Colors
6b449b
f78e1f
ec1f27
ffffff
000000

Requirements
Must have
• eye catching
• "Quillbrook Mist" must be LARGE
• phone number
• website
• areas for flavor name and nicotine strength
• orange, purple, black and red
Nice to have
• clean, abstract vectors
• "corporate look"
• think of a DUNTRA FIZZ can, you immediately know what your'e looking at.
• Our V in vapor is our go to logo
Should not have
• no grunge effects
• no round shapes

```html
<!DOCTYPE html>
<html lang="en">
<head>
<meta charset="utf-8">
<title>Quillbrook Mist – E-Liquid Label</title>
<link rel="stylesheet" href="https://fonts.googleapis.com/css2?family=Arimo:wght@400;700&family=Open+Sans:wght@400&display=swap">
<style>
  :root {
    --purple: #7d4a9e;
    --purple-line: #8a5aa8;
    --orange: #f78e1f;
    --red: #ec1f27;
    --lime: #b5cf3a;
    --ink: #231f20;
    --white: #ffffff;
    --smoke: #ddd3e6;
  }
  * { margin: 0; padding: 0; box-sizing: border-box; }
  html, body { width: 1200px; height: 900px; overflow: hidden; background: var(--white); }
  body { position: relative; font-family: "Arimo", Arial, sans-serif; color: var(--ink); }

  .label {
    position: absolute; left: 188px; top: 123px; width: 826px; height: 451px;
    border: 1px solid #000; background: var(--white); overflow: hidden;
  }
  .label__smoke {
    position: absolute; left: 0; top: 240px; width: 330px; height: 211px;
    background: radial-gradient(ellipse at 30% 70%, var(--smoke) 0%, rgba(221,211,230,0.4) 45%, rgba(255,255,255,0) 75%);
  }
  .contact {
    position: absolute; bottom: 40px;
    display: flex; flex-direction: column; align-items: center; gap: 12px;
    font-family: "Open Sans", Arial, sans-serif; font-size: 17px; color: var(--ink);
  }
  .contact--web { left: 30px; }
  .contact--phone { left: 83px; }
  .contact__text { writing-mode: vertical-rl; transform: rotate(180deg); white-space: nowrap; }
  .contact__icon { width: 26px; height: 26px; }

  .brand {
    position: absolute; left: 0; right: 0; top: 118px; text-align: center;
    font-family: "Arimo", Arial, sans-serif; font-weight: 700; font-size: 54px;
    color: var(--purple); letter-spacing: 0.5px;
  }

  .flavor-rule { position: absolute; width: 82px; height: 14px; border-top: 2px solid var(--purple-line); border-bottom: 2px solid var(--purple-line); top: 288px; }
  .flavor-rule--left { left: 227px; }
  .flavor-rule--right { left: 517px; }
  .flavor-badge {
    position: absolute; left: 317px; top: 200px; width: 190px; height: 190px; border-radius: 50%;
    background: var(--purple); color: var(--white); text-align: center;
  }
  .flavor-badge__name { margin-top: 73px; font-weight: 700; font-size: 34px; }
  .flavor-badge__strength { margin-top: 14px; font-size: 20px; }

  .volume { position: absolute; left: 492px; top: 400px; font-weight: 700; font-size: 24px; }

  .ingredients {
    position: absolute; left: 694px; top: 37px; width: 101px; height: 375px;
    background: var(--ink); border-radius: 8px; color: var(--white);
    display: flex; align-items: center; justify-content: center;
  }
  .ingredients__text {
    writing-mode: vertical-rl; transform: rotate(180deg);
    font-size: 12.4px; line-height: 19px; height: 345px;
  }
  .ingredients__text strong { font-weight: 700; }

  .bottle-lineup {
    position: absolute; left: 112px; top: 600px; width: 262px; height: 282px;
    display: flex; gap: 9px;
  }
  .bottle-lineup__item { flex: 1; border-radius: 20px 20px 14px 14px; }
  .bottle-lineup__item--purple { background: linear-gradient(180deg, #1a1a1a 0 22%, #e9d7b0 22% 40%, #f4eef7 40% 100%); }
  .bottle-lineup__item--lime { background: linear-gradient(180deg, #1a1a1a 0 22%, #e9d7b0 22% 40%, #f3f7e6 40% 100%); }
  .bottle-lineup__item--red { background: linear-gradient(180deg, #1a1a1a 0 22%, #e9d7b0 22% 40%, #fbeaea 40% 100%); }

  .brand-mark {
    position: absolute; left: 820px; top: 782px; font-weight: 700; font-size: 36px; color: var(--purple);
  }
</style>
</head>
<body>
  <section class="label">
    <div class="label__smoke" role="img" aria-label="Soft lavender smoke wisp decoration"></div>

    <div class="contact contact--web">
      <span class="contact__text">http://www.quillbrookmistparlor.com</span>
      <svg class="contact__icon" viewBox="0 0 26 26" aria-hidden="true">
        <circle cx="13" cy="13" r="11" fill="none" stroke="#231f20" stroke-width="2.2"/>
        <ellipse cx="13" cy="13" rx="5" ry="11" fill="none" stroke="#231f20" stroke-width="2"/>
        <line x1="2" y1="13" x2="24" y2="13" stroke="#231f20" stroke-width="2"/>
        <line x1="4" y1="7.5" x2="22" y2="7.5" stroke="#231f20" stroke-width="1.8"/>
        <line x1="4" y1="18.5" x2="22" y2="18.5" stroke="#231f20" stroke-width="1.8"/>
      </svg>
    </div>

    <div class="contact contact--phone">
      <span class="contact__text">(000) 000-0000 • (000) 000-0000</span>
      <svg class="contact__icon" viewBox="0 0 24 24" aria-hidden="true">
        <path fill="#231f20" d="M6.6 10.8a15.1 15.1 0 0 0 6.6 6.6l2.2-2.2a1 1 0 0 1 1-.25 11.4 11.4 0 0 0 3.6.57 1 1 0 0 1 1 1V20a1 1 0 0 1-1 1A17 17 0 0 1 3 4a1 1 0 0 1 1-1h3.5a1 1 0 0 1 1 1c0 1.25.2 2.45.57 3.57a1 1 0 0 1-.25 1z"/>
      </svg>
    </div>

    <h1 class="brand">Quillbrook Mist</h1>

    <div class="flavor-rule flavor-rule--left"></div>
    <div class="flavor-rule flavor-rule--right"></div>
    <div class="flavor-badge">
      <div class="flavor-badge__name">FLAVOR</div>
      <div class="flavor-badge__strength">12mg</div>
    </div>

    <div class="volume">30ml</div>

    <div class="ingredients">
      <p class="ingredients__text"><strong>INGREDIENTS:</strong> Lorem ipsum dolor sit a met, consectetur adipiscing elit, sed do eiusmod tempor incididunt ut labore et dolore magna aliqua. Ut enim ad minimveniam, quis nostrud exercitation ullamco laboris nisi ut aliquip</p>
    </div>
  </section>

  <div class="bottle-lineup" role="img" aria-label="Three dropper bottles wearing the label in purple, lime and red flavor versions">
    <div class="bottle-lineup__item bottle-lineup__item--purple"></div>
    <div class="bottle-lineup__item bottle-lineup__item--lime"></div>
    <div class="bottle-lineup__item bottle-lineup__item--red"></div>
  </div>

  <div class="brand-mark">Quillbrook Mist</div>
</body>
</html>
```